Webdesign für K&L Vendora GmbH
Zielgruppe
- Partner für moderne Automaten- und Verpflegungslösungen in Unternehmen
- Zielgruppe sind Unternehmen, welche Versorgungskonzepte schaffen, die optimal auf die Bedürfnisse von Mitarbeitenden, Kunden und Gästen abgestimmt sind
Aufgabenstellung
- KEINE Kopie der alten Webseite
- Farbkonzept gern in sanften Kaffeetönen kombiniert mit Weiß
- Klare Struktur der Webseite

```html
<!DOCTYPE html>
<html lang="de">
<head>
<meta charset="utf-8">
<title>K&amp;L Vendora GmbH – Automatenlösungen</title>
<link href="https://fonts.googleapis.com/css2?family=Inter:wght@400;500;600;700&family=Inter+Tight:wght@600;700&display=swap" rel="stylesheet">
<style>
:root{
  --brown:#6a3f25;
  --brown-dark:#5a341e;
  --ink:#2a1e17;
  --text:#4b423c;
  --muted:#6f6660;
  --line:#e9e5e1;
  --soft:#f5f3f1;
  --white:#ffffff;
}
*{box-sizing:border-box;margin:0;padding:0}
html,body{width:1200px;height:4069px;overflow:hidden}
body{position:relative;background:var(--white);font-family:"Inter",sans-serif;color:var(--text)}
.abs{position:absolute}
h1,h2,h3{font-family:"Inter Tight",sans-serif;color:var(--ink);font-weight:700;letter-spacing:-0.02em}
.eyebrow{font-size:10px;font-weight:700;letter-spacing:.18em;color:var(--brown);text-transform:uppercase}
.btn{display:inline-flex;align-items:center;gap:8px;height:38px;padding:0 22px;border-radius:10px;font-size:12px;font-weight:600;text-decoration:none}
.btn-primary{background:var(--brown);color:#fff}
.btn-ghost{background:#fff;color:var(--brown);border:1px solid var(--line)}
svg.i{width:16px;height:16px;fill:none;stroke:currentColor;stroke-width:1.8;stroke-linecap:round;stroke-linejoin:round}

/* nav */
.nav{top:0;left:0;width:1200px;height:74px;border-bottom:1px solid #f0ede9}
.brand{font-family:"Inter Tight",sans-serif;font-weight:700;font-size:20px;color:var(--brown);display:flex;align-items:center;gap:8px}
.brand .sq{width:12px;height:12px;background:var(--brown)}
.nav .brand{position:absolute;left:115px;top:25px}
.nav-links{position:absolute;left:595px;top:34px;display:flex;gap:22px;font-size:12px;font-weight:500;color:var(--ink)}
.nav .btn{position:absolute;left:941px;top:28px;height:30px;padding:0 14px;font-size:11.5px}

/* hero */
.hero-loc{top:146px;left:115px;display:flex;align-items:center;gap:8px;border-left:2px solid var(--brown);padding-left:10px}
.hero h1{top:178px;left:114px;width:580px;font-size:58px;line-height:62px}
.hero-lead{top:450px;left:115px;width:560px;font-size:14px;line-height:25px}
.hero-actions{top:522px;left:115px;display:flex;gap:10px}
.hero-checks{top:597px;left:115px;width:560px;border-top:1px solid var(--line);padding-top:16px;display:flex;gap:24px;font-size:10.5px;font-weight:600;color:var(--ink)}
.hero-checks span{display:flex;gap:6px;align-items:center}
.hero-checks svg{width:11px;height:11px}
.hero-media{top:139px;left:723px;width:367px;height:462px;border-radius:8px;background:linear-gradient(160deg,#3a2a20 0%,#1f1814 45%,#6b4a33 100%)}

/* solutions */
.sol-eyebrow{top:726px;left:115px}
.sol h2{top:746px;left:114px;font-size:40px;line-height:39px;width:600px}
.sol-lead{top:842px;left:115px;width:560px;font-size:14px;line-height:22px}
.sol-aside{top:848px;left:778px;width:310px;font-size:11.5px;line-height:20px;color:var(--muted)}
.card{top:928px;width:316px;height:356px;border:1px solid var(--line);border-radius:14px;overflow:hidden;background:#fff}
.card-media{height:206px;background:var(--soft);display:flex;align-items:center;justify-content:center}
.card-media div{width:60px;height:152px;border-radius:4px}
.card-body{padding:22px 19px}
.card-ico{width:30px;height:30px;border-radius:50%;background:#f3ece6;color:var(--brown);display:flex;align-items:center;justify-content:center;margin-bottom:18px}
.card-ico svg{width:14px;height:14px}
.card h3{font-size:17px;margin-bottom:10px}
.card p{font-size:11.5px;line-height:19px;color:var(--muted)}
.arrow{top:1095px;width:22px;height:22px;border-radius:50%;background:#fff;border:1px solid var(--line);display:flex;align-items:center;justify-content:center;color:var(--ink)}
.arrow svg{width:11px;height:11px}

/* about band */
.about{top:1388px;left:63px;width:1074px;height:377px;border-radius:28px;background:var(--brown)}
.about .eyebrow{position:absolute;left:52px;top:92px;color:#d9c3b2}
.about h2{position:absolute;left:51px;top:110px;width:470px;font-size:40px;line-height:39px;color:#fff}
.about-copy{position:absolute;left:560px;top:88px;width:460px;color:#ead9cc;font-size:12.5px;line-height:26px}
.about-copy strong{display:block;color:#fff;font-size:15.5px;line-height:23px;font-weight:600;margin-bottom:16px}
.about-copy p{margin-bottom:16px}

/* service */
.svc-eyebrow{top:1874px;left:115px}
.svc h2{top:1890px;left:114px;font-size:40px;line-height:39px;width:600px}
.svc-lead{top:1989px;left:115px;width:560px;font-size:14px;line-height:22px}
.steps{top:2076px;left:114px;width:972px;height:186px;border:1px solid var(--line);border-radius:14px;display:grid;grid-template-columns:repeat(4,1fr)}
.step{padding:26px 28px;border-right:1px solid var(--line);position:relative}
.step:last-child{border-right:0}
.step .num{font-size:10px;font-weight:600;letter-spacing:.12em;color:var(--ink)}
.step svg{position:absolute;right:28px;top:24px;width:18px;height:18px;color:var(--brown)}
.step h3{font-size:17px;margin-top:46px;margin-bottom:10px}
.step p{font-size:11.5px;line-height:19px;color:var(--muted)}

/* why */
.why{top:2378px;left:63px;width:1074px;height:480px;border-radius:28px;background:var(--soft)}
.why .eyebrow{position:absolute;left:52px;top:66px}
.why h2{position:absolute;left:51px;top:84px;width:600px;font-size:40px;line-height:39px}
.why-lead{position:absolute;left:52px;top:180px;width:560px;font-size:14px;line-height:22px}
.why-grid{position:absolute;left:52px;top:292px;display:grid;grid-template-columns:repeat(3,300px);gap:30px}
.why-grid svg{width:18px;height:18px;color:var(--brown)}
.why-grid h3{font-size:16px;margin:20px 0 10px}
.why-grid p{font-size:11.5px;line-height:19px;color:var(--muted)}

/* faq */
.faq-eyebrow{top:2975px;left:115px}
.faq h2{top:2992px;left:114px;width:380px;font-size:40px;line-height:39px}
.faq-lead{top:3092px;left:115px;width:340px;font-size:14px;line-height:22px}
.faq-list{top:2975px;left:526px;width:560px;border-top:1px solid var(--line)}
.faq-item{height:83px;border-bottom:1px solid var(--line);padding-top:20px;position:relative}
.faq-item h3{font-family:"Inter",sans-serif;font-size:12.5px;font-weight:600;letter-spacing:0;margin-bottom:16px}
.faq-item p{font-size:11px;color:var(--muted)}
.faq-item svg{position:absolute;right:8px;top:20px;width:12px;height:12px;color:var(--ink)}

/* contact */
.contact{top:3430px;left:63px;width:1074px;height:518px;border-radius:28px;background:var(--brown)}
.contact .eyebrow{position:absolute;left:52px;top:63px;color:#d9c3b2}
.contact h2{position:absolute;left:51px;top:80px;width:420px;font-size:40px;line-height:39px;color:#fff}
.contact-lead{position:absolute;left:52px;top:214px;width:420px;font-size:12.5px;line-height:24px;color:#ead9cc}
.contact-list{position:absolute;left:52px;top:290px;list-style:none;color:#fff;font-size:11.5px}
.contact-list li{display:flex;gap:10px;align-items:center;margin-bottom:13px}
.contact-list svg{width:14px;height:14px}
.form{position:absolute;left:482px;top:57px;width:541px;height:407px;background:#fff;border-radius:18px;padding:38px 26px 0}
.form label{display:block;font-size:11px;font-weight:600;color:var(--ink);margin-bottom:10px}
.row{display:grid;grid-template-columns:1fr 1fr;gap:16px;margin-bottom:26px}
.field{height:36px;border:1px solid var(--line);border-radius:8px}
.area{height:90px;border:1px solid var(--line);border-radius:8px}
.form .btn{width:100%;justify-content:center;height:36px;margin-top:22px;font-size:11.5px}
.form small{display:block;font-size:9.5px;color:var(--muted);margin-top:14px}

/* footer */
.footer{top:4000px;left:0;width:1200px}
.footer .brand{position:absolute;left:115px;top:0;font-size:18px}
.footer-links{position:absolute;left:829px;top:11px;display:flex;gap:22px;font-size:10.5px;color:var(--muted)}
</style>
</head>
<body>

<header class="abs nav">
  <div class="brand"><span class="sq"></span>K&amp;L Vendora</div>
  <nav class="nav-links"><span>Lösungen</span><span>Service</span><span>Unternehmen</span><span>FAQ</span></nav>
  <a class="btn btn-primary" href="#kontakt">Beratung anfragen <svg class="i" viewBox="0 0 24 24" style="width:12px;height:12px"><path d="M5 12h14M13 6l6 6-6 6"/></svg></a>
</header>

<section class="hero">
  <div class="abs hero-loc eyebrow"><svg class="i" viewBox="0 0 24 24" style="width:12px;height:12px"><path d="M12 21s7-6.5 7-12a7 7 0 0 0-14 0c0 5.5 7 12 7 12z"/><circle cx="12" cy="9" r="2.5"/></svg>Chemnitz · Sachsen</div>
  <h1 class="abs">Automatenlösungen, die Ihren Arbeitsalltag bereichern.</h1>
  <p class="abs hero-lead">Moderne Getränke-, Snack- und Wasserversorgung für Unternehmen. Individuelle Versorgungskonzepte für Mitarbeitende, Kunden und Gäste.</p>
  <div class="abs hero-actions">
    <a class="btn btn-primary" href="#kontakt">Jetzt beraten lassen <svg class="i" viewBox="0 0 24 24" style="width:12px;height:12px"><path d="M5 12h14M13 6l6 6-6 6"/></svg></a>
    <a class="btn btn-ghost" href="#loesungen">Produkte entdecken</a>
  </div>
  <div class="abs hero-checks">
    <span><svg class="i" viewBox="0 0 24 24"><path d="M5 12l5 5 9-10"/></svg>Persönlicher Service</span>
    <span><svg class="i" viewBox="0 0 24 24"><path d="M5 12l5 5 9-10"/></svg>Sachsenweit verfügbar</span>
    <span><svg class="i" viewBox="0 0 24 24"><path d="M5 12l5 5 9-10"/></svg>Installation &amp; Wartung</span>
    <span><svg class="i" viewBox="0 0 24 24"><path d="M5 12l5 5 9-10"/></svg>Alles aus einer Hand</span>
  </div>
  <div class="abs hero-media" role="img" aria-label="Zwei Getränke- und Snackautomaten mit Kaffeebohnen-Motiv"></div>
</section>

<section class="sol" id="loesungen">
  <div class="abs eyebrow sol-eyebrow">Unsere Lösungen</div>
  <h2 class="abs">Versorgung, die zu Ihrem Unternehmen passt.</h2>
  <p class="abs sol-lead">Von der kompakten Kaffeelösung bis zur kompletten Rundumverpflegung – wir planen passend zu Standort, Teamgröße und Bedarf.</p>
  <p class="abs sol-aside">Keine Lösung von der Stange. Sondern leistungsstarke Technik, abgestimmt auf Ihren Arbeitsalltag.</p>

  <article class="abs card" style="left:114px">
    <div class="card-media"><div role="img" aria-label="Blauer Snackautomat" style="background:linear-gradient(180deg,#2d6fd1,#1b4fa8)"></div></div>
    <div class="card-body">
      <div class="card-ico"><svg class="i" viewBox="0 0 24 24"><path d="M5 9h11v6a4 4 0 0 1-4 4H9a4 4 0 0 1-4-4z"/><path d="M16 11h2a2 2 0 0 1 0 4h-2"/></svg></div>
      <h3>InCup-Systeme</h3>
      <p>Schnelle, saubere und praktische Getränkezubereitung.</p>
    </div>
  </article>
  <article class="abs card" style="left:442px">
    <div class="card-media"><div role="img" aria-label="Standgerät für Heißgetränke" style="background:linear-gradient(180deg,#3b3633,#6d6863)"></div></div>
    <div class="card-body">
      <div class="card-ico"><svg class="i" viewBox="0 0 24 24"><ellipse cx="12" cy="12" rx="5" ry="8" transform="rotate(40 12 12)"/><path d="M8 16c3-2 5-6 8-8"/></svg></div>
      <h3>Standgeräte</h3>
      <p>Flexible Lösungen für verschiedene Einsatzbereiche.</p>
    </div>
  </article>
  <article class="abs card" style="left:770px">
    <div class="card-media"><div role="img" aria-label="Kaltgetränke- und Kaffeeautomat" style="width:84px;height:150px;background:linear-gradient(180deg,#1c1c1c 60%,#bdbdbd)"></div></div>
    <div class="card-body">
      <div class="card-ico"><svg class="i" viewBox="0 0 24 24"><path d="M12 3s6 6 6 11a6 6 0 0 1-12 0c0-5 6-11 6-11z"/></svg></div>
      <h3>Kaltgetränkeautomaten</h3>
      <p>Gekühlte Erfrischungen jederzeit verfügbar.</p>
    </div>
  </article>
  <div class="abs arrow" style="left:103px"><svg class="i" viewBox="0 0 24 24"><path d="M19 12H5M11 6l-6 6 6 6"/></svg></div>
  <div class="abs arrow" style="left:1075px"><svg class="i" viewBox="0 0 24 24"><path d="M5 12h14M13 6l6 6-6 6"/></svg></div>
</section>

<section class="abs about">
  <div class="eyebrow">K&amp;L Vendora GmbH</div>
  <h2>Ihr zuverlässiger Partner für moderne Automatenlösungen</h2>
  <div class="about-copy">
    <strong>Getränkeautomaten, Snackautomaten, InCup-Systeme, Wasserspender &amp; Standgeräte für Unternehmen.</strong>
    <p>Die K&amp;L Vendora GmbH ist Ihr zuverlässiger Partner für moderne Automatenlösungen in Chemnitz und ganz Sachsen.</p>
    <p>Wir entwickeln individuelle Versorgungskonzepte für Unternehmen, Büros und Betriebe – effizient, hygienisch und passgenau auf Ihre Anforderungen abgestimmt.</p>
  </div>
</section>

<section class="svc">
  <div class="abs eyebrow svc-eyebrow">Alles aus einer Hand</div>
  <h2 class="abs">Rundum-Service für Ihre Automaten</h2>
  <p class="abs svc-lead">Von der persönlichen Beratung über die Installation bis hin zur regelmäßigen Wartung und Befüllung kümmern wir uns um den kompletten Betrieb.</p>
  <div class="abs steps">
    <div class="step"><span class="num">01</span><svg class="i" viewBox="0 0 24 24"><path d="M21 12a8 8 0 0 1-11.5 7.2L4 20l1.2-4.5A8 8 0 1 1 21 12z"/></svg><h3>Beratung</h3><p>Bedarf und Standort gemeinsam analysieren.</p></div>
    <div class="step"><span class="num">02</span><svg class="i" viewBox="0 0 24 24"><circle cx="12" cy="12" r="3"/><path d="M12 2v3M12 19v3M2 12h3M19 12h3M4.9 4.9l2.1 2.1M17 17l2.1 2.1M4.9 19.1L7 17M17 7l2.1-2.1"/></svg><h3>Planung</h3><p>Ein wirtschaftliches Konzept entwickeln.</p></div>
    <div class="step"><span class="num">03</span><svg class="i" viewBox="0 0 24 24"><path d="M14.7 6.3a4 4 0 0 0 5 5L13 18l-3 3-4-4 3-3z"/><path d="M14.7 6.3L17 4"/></svg><h3>Installation</h3><p>Sicher aufstellen und betriebsbereit übergeben.</p></div>
    <div class="step"><span class="num">04</span><svg class="i" viewBox="0 0 24 24"><path d="M12 3l7 3v6c0 4.5-3 7.5-7 9-4-1.5-7-4.5-7-9V6z"/><path d="M9 12l2 2 4-4"/></svg><h3>Betrieb</h3><p>Regelmäßig warten, befüllen und betreuen.</p></div>
  </div>
</section>

<section class="abs why">
  <div class="eyebrow">Warum K&amp;L</div>
  <h2>Partnerschaft, auf die Sie sich verlassen können.</h2>
  <p class="why-lead">Als regionaler Anbieter stehen wir für Qualität, Zuverlässigkeit und persönlichen Service – für zufriedene Mitarbeitende und einen professionellen Eindruck bei Ihren Kunden.</p>
  <div class="why-grid">
    <div><svg class="i" viewBox="0 0 24 24"><path d="M12 21s7-6.5 7-12a7 7 0 0 0-14 0c0 5.5 7 12 7 12z"/><circle cx="12" cy="9" r="2.5"/></svg><h3>Regional nah</h3><p>Direkte Ansprechpartner und zuverlässiger Service in Chemnitz und ganz Sachsen.</p></div>
    <div><svg class="i" viewBox="0 0 24 24"><rect x="4" y="5" width="16" height="16" rx="1"/><path d="M8 9h2M14 9h2M8 13h2M14 13h2M10 21v-4h4v4"/></svg><h3>Individuell geplant</h3><p>Jede Lösung orientiert sich an Ihren Räumen, Abläufen und Anforderungen.</p></div>
    <div><svg class="i" viewBox="0 0 24 24"><path d="M12 3l7 3v6c0 4.5-3 7.5-7 9-4-1.5-7-4.5-7-9V6z"/><path d="M9 12l2 2 4-4"/></svg><h3>Dauerhaft betreut</h3><p>Wir bleiben an Ihrer Seite – von der ersten Idee bis zum laufenden Betrieb.</p></div>
  </div>
</section>

<section class="faq">
  <div class="abs eyebrow faq-eyebrow">Gut zu wissen</div>
  <h2 class="abs">Häufig gestellte Fragen</h2>
  <p class="abs faq-lead">Sie haben eine andere Frage? Sprechen Sie uns persönlich an – wir beraten Sie gern.</p>
  <div class="abs faq-list">
    <div class="faq-item"><h3>Betreuen Sie Unternehmen in ganz Sachsen?</h3><p>Ja, wir betreuen Unternehmen in Chemnitz und ganz Sachsen.</p><svg class="i" viewBox="0 0 24 24"><path d="M6 15l6-6 6 6"/></svg></div>
    <div class="faq-item"><h3>Übernehmen Sie auch Wartung und Befüllung?</h3><p>Ja, wir kümmern uns um den kompletten Betrieb Ihrer Automaten.</p><svg class="i" viewBox="0 0 24 24"><path d="M6 15l6-6 6 6"/></svg></div>
    <div class="faq-item"><h3>Welche Automaten bieten Sie an?</h3><p>InCup-Systeme, Standgeräte, Kaltgetränkeautomaten, Snackautomaten und Wasserspender.</p><svg class="i" viewBox="0 0 24 24"><path d="M6 15l6-6 6 6"/></svg></div>
    <div class="faq-item"><h3>Gibt es individuelle Versorgungskonzepte?</h3><p>Ja, jede Lösung wird individuell auf die Anforderungen Ihres Unternehmens abgestimmt.</p><svg class="i" viewBox="0 0 24 24"><path d="M6 15l6-6 6 6"/></svg></div>
  </div>
</section>

<section class="abs contact" id="kontakt">
  <div class="eyebrow">Kontakt</div>
  <h2>Lassen Sie uns Ihre Versorgung neu denken.</h2>
  <p class="contact-lead">Gemeinsam entwickeln wir die passende Automatenlösung für Ihr Unternehmen.</p>
  <ul class="contact-list">
    <li><svg class="i" viewBox="0 0 24 24"><rect x="3" y="5" width="18" height="14" rx="2"/><path d="M3 7l9 6 9-6"/></svg>info@kl-vendora.de</li>
    <li><svg class="i" viewBox="0 0 24 24"><path d="M12 21s7-6.5 7-12a7 7 0 0 0-14 0c0 5.5 7 12 7 12z"/><circle cx="12" cy="9" r="2.5"/></svg>Standort in der Kartenansicht öffnen</li>
    <li><svg class="i" viewBox="0 0 24 24"><path d="M5 4h4l2 5-2.5 1.5a11 11 0 0 0 5 5L15 13l5 2v4a2 2 0 0 1-2 2A16 16 0 0 1 3 6a2 2 0 0 1 2-2"/></svg>Persönliche Beratung in Chemnitz &amp; Sachsen</li>
  </ul>
  <form class="form">
    <div class="row">
      <div><label>Name</label><div class="field"></div></div>
      <div><label>Unternehmen</label><div class="field"></div></div>
    </div>
    <div style="margin-bottom:26px"><label>E-Mail</label><div class="field"></div></div>
    <div><label>Wie können wir helfen?</label><div class="area"></div></div>
    <a class="btn btn-primary" href="#kontakt">Beratung anfragen <svg class="i" viewBox="0 0 24 24" style="width:12px;height:12px"><path d="M5 12h14M13 6l6 6-6 6"/></svg></a>
    <small>Mit dem Absenden stimmen Sie der Verarbeitung Ihrer Angaben zur Bearbeitung Ihrer Anfrage zu.</small>
  </form>
</section>

<footer class="abs footer">
  <div class="brand"><span class="sq"></span>K&amp;L Vendora</div>
  <div class="footer-links"><span>Impressum</span><span>Datenschutz</span><span>Erklärung zur Barrierefreiheit</span></div>
</footer>

</body>
</html>
```